independent cleaner, reliable, custom, thorough, trustworthy

Not sure yet if I want single-sided or double sided, so I'm selecting double-sided just in case, but single-sided designs are okay.

Really looking to find the happy medium between personal and professional in a business card design. I end up building comfortable relationships with the people I work for.

Most of my business is through referrals, but I want some business cards to hand out to people who ask for one (and maybe put them on community bulletin boards).

My target market is homeowners and business owners who are looking for a reliable cleaner and are willing to pay a bit more to have excellent quality and someone they trust.

Theme: I have a personal-professional feel since I'm solo, so the theme should reflect that. Trustworthy, personal, simple. I clean up messes.

Hopefully this is enough info, let me know if you have any questions though of course!

Target Market(s)

Homeowners businessowners who are looking for a reliable cleaner, excellent quality trustworthy.

Industry/Entity Type

Cleaning Service

Contact Information for Business Card

Please include this text:
• Delphine Marrow
• independent cleaner
• reliable, custom, thorough
• 604-317-2296
• tbw.marrow@quillpost.net

Font styles to use
Serif
Sans Serif

Colors
ffffff
00a990
0492cd
33a6d7
0355a3
3276b5
919191

Requirements
Must have
• Really looking to find the happy medium between personal and professional in a business card design.
• Background: at least 50% white on the side with the most text (coloured accents or shapes are okay)
• I lean more towards simple and clean, solid colours, maybe a gentle gradient
Nice to have
• Not sure yet if I want single-sided or double sided, so I'm selecting double-sided just in case, but single-sided designs are okay.
• Colours: preferably blues and teals for the font and other objects (if any). Open to designer's choice though. I've toyed around with orangey-yellow, but it doesn't feel right and I keep going back to blues/teals
• Also I uploaded a sketch of my signature and initials so you can get a feel for my personality. I'm not expecting this to be included in the design, it's just there.
Should not have
• I don't like a lot of busy-ness or textures
• Also I don't have a logo (not sure where else to specify this)

```html
<!DOCTYPE html>
<html lang="en">
<head>
<meta charset="utf-8">
<title>Delphine Marrow — Business Card</title>
<link rel="stylesheet" href="https://fonts.googleapis.com/css2?family=Montserrat:wght@400;500&family=Yellowtail&display=swap">
<style>
  :root {
    --page: #d9d9d7;
    --white: #ffffff;
    --blue: #2a86c4;
    --blue-deep: #2b7cc0;
    --teal: #1aa98f;
    --ink: #4a4a4a;
  }
  * { margin: 0; padding: 0; box-sizing: border-box; }
  html, body {
    width: 1200px; height: 801px; overflow: hidden;
    background: var(--page);
    font-family: "Montserrat", Arial, sans-serif;
  }
  .stage {
    width: 1200px; height: 801px;
    display: flex; align-items: center; justify-content: center; gap: 50px;
  }
  .card {
    position: relative;
    width: 540px; height: 309px;
    border-radius: 3px;
    overflow: hidden;
    box-shadow: 0 6px 18px rgba(0,0,0,0.18);
  }
  .card--front { background: var(--white); }
  .card--back { background: var(--blue); display: flex; align-items: center; justify-content: center; }
  .front-band { position: absolute; inset: 0; width: 100%; height: 100%; }
  .identity { position: absolute; left: 64px; top: 62px; }
  .identity__name {
    font-family: "Yellowtail", "Brush Script MT", cursive;
    font-weight: 400;
    font-size: 48px; color: var(--blue-deep); line-height: 1.1;
    white-space: nowrap;
  }
  .identity__role {
    margin: 4px 0 0 92px;
    font-size: 13px; font-weight: 400; color: var(--ink); letter-spacing: 0.3px;
    white-space: nowrap;
  }
  .tagline {
    position: absolute; left: 252px; top: 230px;
    font-size: 14px; color: var(--white); letter-spacing: 0.4px;
    white-space: nowrap;
  }
  .contacts {
    position: absolute; left: 196px; top: 272px;
    display: flex; gap: 24px;
    font-size: 11px; color: var(--white); letter-spacing: 0.3px;
    white-space: nowrap;
  }
  .contact { display: flex; align-items: center; gap: 7px; white-space: nowrap; }
  .contact svg { width: 12px; height: 12px; flex: none; fill: none; stroke: var(--white); stroke-width: 1.6; }
  .back-name {
    font-family: "Montserrat", Arial, sans-serif;
    font-weight: 500; font-size: 30px;
    color: var(--teal); letter-spacing: 1px;
    white-space: nowrap;
  }
</style>
</head>
<body>
<main class="stage">
  <section class="card card--front">
    <svg class="front-band" viewBox="0 0 540 309" aria-hidden="true">
      <path d="M140 309 L285 160 Q306 140 300 172 L292 200 L540 62 L540 309 Z" fill="var(--teal)"/>
      <path d="M158 309 L290 175 Q300 168 296 190 L292 214 L540 76 L540 309 Z" fill="var(--blue)"/>
    </svg>
    <div class="identity">
      <h1 class="identity__name">Delphine Marrow</h1>
      <p class="identity__role">Independent cleaner</p>
    </div>
    <p class="tagline">Reliable, custom, thorough</p>
    <div class="contacts">
      <span class="contact">
        <svg viewBox="0 0 12 12"><path d="M3 1 L5 3.5 L4 5 Q5 7 7 8 L8.5 7 L11 9 L9.5 11 Q4 10 1 3 Z"/></svg>
        604-317-2296
      </span>
      <span class="contact">
        <svg viewBox="0 0 12 12"><rect x="1" y="2.5" width="10" height="7"/><path d="M1 2.5 L6 6.5 L11 2.5"/></svg>
        tbw.marrow@quillpost.net
      </span>
    </div>
  </section>
  <section class="card card--back">
    <p class="back-name">Delphine Marrow</p>
  </section>
</main>
</body>
</html>
```